Billboard Design for Equipment Rental Business

We need a billboard design for our equipment rental business called Brindlewood Equipment Company. We are based in Georgia. We rent construction tools, equipment, and dumpsters. We currently have a design but feel like we could get something better. Our phone number is 912-730-2591 and our website is www.brindlewoodequipment-example.com

```html
<!DOCTYPE html>
<html lang="en">
<head>
<meta charset="UTF-8">
<title>Brindlewood Equipment Company – Billboard</title>
<link rel="stylesheet" href="https://fonts.googleapis.com/css2?family=Poppins:wght@600;700;800&family=Barlow+Condensed:wght@700;800&display=swap">
<style>
  :root {
    --yellow: #f7b81c;
    --black: #0c0c0c;
    --white: #ffffff;
    --white-shade: #d9d9d9;
  }
  * { margin: 0; padding: 0; box-sizing: border-box; }
  html, body { width: 1200px; height: 821px; overflow: hidden; background: var(--black); }
  .billboard { position: relative; width: 1200px; height: 821px; overflow: hidden; }

  .brand-band { position: absolute; left: 0; top: 0; width: 1200px; height: 330px; background: var(--yellow); }
  .brand-mark { position: absolute; left: 70px; top: 80px; width: 150px; height: 150px; background: var(--black); }
  .brand-name {
    position: absolute; left: 265px; top: 58px;
    font-family: 'Poppins', sans-serif; font-weight: 800; color: var(--black);
    line-height: 1;
  }
  .brand-name .primary { display: block; font-size: 104px; letter-spacing: 1px; }
  .brand-name .secondary { display: block; font-size: 44px; letter-spacing: 6px; margin-top: 18px; }

  .offer-band { position: absolute; left: 0; top: 330px; width: 1200px; height: 228px; background: var(--black); }
  .offer-tag { position: absolute; left: 0; top: 0; width: 1200px; height: 140px; }
  .offer-title {
    position: absolute; left: 0; top: 330px; width: 1200px; height: 140px;
    display: flex; align-items: center; justify-content: center;
    font-family: 'Barlow Condensed', sans-serif; font-weight: 800;
    font-size: 150px; color: var(--black); letter-spacing: 1px; line-height: 1;
  }
  .service-list {
    position: absolute; left: 0; top: 470px; width: 1200px; height: 88px;
    display: flex; align-items: center; justify-content: center; gap: 22px;
    list-style: none;
    font-family: 'Barlow Condensed', sans-serif; font-weight: 700;
    font-size: 76px; color: var(--yellow); line-height: 1;
  }
  .service-list li { display: flex; align-items: center; gap: 14px; }
  .service-icon { width: 50px; height: 50px; border: 4px solid var(--yellow); border-radius: 8px; }

  .phone-band {
    position: absolute; left: 0; top: 558px; width: 1200px; height: 150px; background: var(--yellow);
    display: flex; align-items: center; justify-content: center;
    font-family: 'Poppins', sans-serif; font-weight: 800; font-size: 132px;
    color: var(--black); letter-spacing: -2px; line-height: 1;
  }
  .web-band {
    position: absolute; left: 0; top: 708px; width: 1200px; height: 113px; background: var(--black);
    display: flex; align-items: center; justify-content: center;
    font-family: 'Poppins', sans-serif; font-weight: 600; font-size: 34px;
    color: var(--yellow); letter-spacing: 3px; text-transform: uppercase;
  }
</style>
</head>
<body>
<main class="billboard">
  <header class="brand-band">
    <div class="brand-mark"></div>
    <h1 class="brand-name">
      <span class="primary">BRINDLEWOOD</span>
      <span class="secondary">EQUIPMENT COMPANY</span>
    </h1>
  </header>

  <section class="offer-band">
    <svg class="offer-tag" viewBox="0 0 1200 140" aria-hidden="true">
      <defs>
        <linearGradient id="tagShade" x1="0" x2="1" y1="0" y2="0">
          <stop offset="0" stop-color="var(--white-shade)"/>
          <stop offset="0.35" stop-color="var(--white)"/>
          <stop offset="1" stop-color="var(--white-shade)"/>
        </linearGradient>
      </defs>
      <polygon points="170,0 1030,0 985,140 215,140" fill="url(#tagShade)"/>
    </svg>
  </section>
  <h2 class="offer-title">WE RENT</h2>

  <ul class="service-list">
    <li><span class="service-icon" role="img" aria-label="Tools icon"></span>TOOLS</li>
    <li><span class="service-icon" role="img" aria-label="Excavator icon"></span>EQUIPMENT</li>
    <li><span class="service-icon" role="img" aria-label="Dumpster icon"></span>DUMPSTERS</li>
  </ul>

  <div class="phone-band">912-730-2591</div>
  <footer class="web-band">www.brindlewoodequipment-example.com</footer>
</main>
</body>
</html>
```